Economics and Investing for women with a humorous narrative

I need a logo and business card design for my company:
The Velvet Sparrow LLC. TVS is an educational website dedicated to translating the language of economics and investing into concepts that are interesting, easy to understand and funny.
As the target market is for women, the card needs to be NON traditional in terms of finance and investing. No pictures of charts, currencies, stock markets etc. This needs to be colorful , inviting and memorable.
The driver of the site is to present difficult concepts with a humorous tilt. If Dorian Hale (The Paper Orchard) collaborated with Jolene Pratt what would it look like?

Reason: I don't think I did a good enough job of explaining what I was looking for including the type of color palette. I asked that the cards NOT look so corporate. I have updated my brief and included 3 pictures of a color scheme I like along with design. I also update the information to be included on the card.

Target Market(s)

Women 30-50

Industry/Entity Type

Business

Contact Information for Business Card

The Velvet Sparrow LLC
Wanda Klose , CEO
382 Garnet Street
Suite 2700
New York, New York 10122

Phone: 212-555-0143
TheVelvetSparrow.com
Email: wanda@thevelvetsparrow.com

Font styles to use
Other font styles liked:
• LustPro Demi No.3

Requirements
Must have
• Gravitas, bold warm colors, the antithesis of modest
Nice to have
• Isn't this why I am hiring designers?
Should not have
• Charts, graphs, numbers, currency, stock or bond market pictures, any reference to investing . Do not want this to look like a boring investment business card

```html
<!DOCTYPE html>
<html lang="en">
<head>
<meta charset="utf-8">
<title>The Velvet Sparrow LLC — Business Card</title>
<link rel="stylesheet" href="https://fonts.googleapis.com/css2?family=Abhaya+Libre:wght@400;500;600&display=swap">
<style>
  :root {
    --canvas-bg: #e4e4e4;
    --paper: #ffffff;
    --ink: #0a0a0a;
    --black-band: #020203;
    --wine: #7a1c1c;
    --wine-deep: #530000;
    --wine-text: #7b1414;
    --white: #ffffff;
  }
  * { margin: 0; padding: 0; box-sizing: border-box; }
  html, body {
    width: 1189px; height: 1200px; overflow: hidden;
    background: var(--canvas-bg);
  }
  .canvas { position: relative; width: 1189px; height: 1200px; }
  .card {
    position: absolute; left: 140px; width: 918px; height: 524px;
    overflow: hidden;
    box-shadow: 0 6px 14px rgba(0,0,0,0.25);
    font-family: "Abhaya Libre", Georgia, serif;
  }
  .card--front { top: 45px; background: var(--paper); }
  .card--back {
    top: 624px;
    background: linear-gradient(to bottom, var(--wine-deep) 0%, var(--wine-deep) 28%, var(--wine) 62%, #6e1a1a 100%);
  }
  .wave { position: absolute; left: 0; top: 0; width: 918px; height: 524px; }
  .holder {
    position: absolute; right: 88px; top: 36px; text-align: right;
    color: var(--wine-text);
  }
  .holder__name { font-size: 52px; font-weight: 600; line-height: 1; }
  .holder__title { font-size: 29px; font-weight: 400; line-height: 1; margin-top: 4px; }
  .company-name {
    position: absolute; right: 88px; top: 138px;
    font-size: 57px; font-weight: 500; color: var(--ink); line-height: 1; white-space: nowrap;
  }
  .contact {
    position: absolute; right: 87px; top: 298px; list-style: none;
    color: var(--white); font-size: 26px; line-height: 1;
  }
  .contact__row {
    display: flex; justify-content: flex-end; align-items: center;
    height: 40.5px;
  }
  .contact__text { text-align: right; white-space: nowrap; }
  .contact__icon {
    width: 21px; height: 21px; margin-left: 27px; flex: none;
    background: var(--white); border-radius: 2px;
    display: flex; align-items: center; justify-content: center;
  }
  .contact__icon--none { background: none; }
  .contact__icon svg { width: 15px; height: 15px; display: block; }
  .back-name {
    position: absolute; left: 0; right: 0; top: 208px; text-align: center;
    color: var(--white); font-size: 57px; font-weight: 500; line-height: 66px;
  }
</style>
</head>
<body>
<main class="canvas">
  <section class="card card--front" aria-label="Business card front">
    <svg class="wave" viewBox="0 0 918 524" aria-hidden="true">
      <defs>
        <linearGradient id="band-red" x1="0" y1="0" x2="1" y2="0">
          <stop offset="0" stop-color="#6b1818"/>
          <stop offset="0.35" stop-color="#7d1d1d"/>
          <stop offset="0.7" stop-color="#5a1010"/>
          <stop offset="1" stop-color="#3a0808"/>
        </linearGradient>
      </defs>
      <path d="M0 259 C90 290 160 310 260 304 C420 294 560 220 700 222 C790 224 860 270 918 303 L918 524 L0 524 Z" fill="url(#band-red)"/>
      <path d="M0 318 C80 340 150 355 240 350 C420 340 580 240 760 241 C840 242 890 280 918 302 L918 524 L0 524 Z" fill="var(--black-band)"/>
    </svg>

    <div class="holder">
      <p class="holder__name">Wanda Klose</p>
      <p class="holder__title">CEO</p>
    </div>
    <h1 class="company-name">The Velvet Sparrow LLC</h1>

    <ul class="contact">
      <li class="contact__row">
        <span class="contact__text">212-555-0143</span>
        <span class="contact__icon"><svg viewBox="0 0 16 16"><path d="M4 1.5 L6.5 4.5 L5.2 6.2 C6 8 7.7 9.8 9.6 10.8 L11.3 9.5 L14.5 12 L12.8 14.5 C7.5 13.5 2.5 8.5 1.5 3.2 Z" fill="var(--ink)"/></svg></span>
      </li>
      <li class="contact__row">
        <span class="contact__text">thevelvetsparrow.com</span>
        <span class="contact__icon"><svg viewBox="0 0 16 16"><circle cx="8" cy="8" r="6.8" fill="var(--ink)"/><path d="M5 4 C7 5 6 7 8 8 C9 10 7 11 8 13.5 M10 3.5 C10.5 5 12 5.5 13.5 6" stroke="var(--white)" stroke-width="1.4" fill="none"/></svg></span>
      </li>
      <li class="contact__row">
        <span class="contact__text">wanda@thevelvetsparrow.com</span>
        <span class="contact__icon"><svg viewBox="0 0 16 16"><rect x="1.5" y="3.5" width="13" height="9" fill="var(--ink)"/><path d="M1.8 4 L8 9 L14.2 4" stroke="var(--white)" stroke-width="1.2" fill="none"/></svg></span>
      </li>
      <li class="contact__row">
        <span class="contact__text">382 Garnet Street Suite 2700 New York</span>
        <span class="contact__icon"><svg viewBox="0 0 16 16"><path d="M8 1.5 C5.2 1.5 3.5 3.5 3.5 6 C3.5 9 8 14.5 8 14.5 C8 14.5 12.5 9 12.5 6 C12.5 3.5 10.8 1.5 8 1.5 Z" fill="var(--ink)"/><circle cx="8" cy="6" r="1.7" fill="var(--white)"/></svg></span>
      </li>
      <li class="contact__row">
        <span class="contact__text">New York 10122</span>
        <span class="contact__icon contact__icon--none"></span>
      </li>
    </ul>
  </section>

  <section class="card card--back" aria-label="Business card back">
    <h2 class="back-name">The Velvet Sparrow<br>LLC</h2>
  </section>
</main>
</body>
</html>
```